Business Card Design Project

I'm moving my dental office and would like to use my existing logo to create a new:
- Business Card (submit here)
- Appointment Card (please submit to this project - http://tasks.pixelbazaar.net/task.aspx?id=493261)
- Letterhead (please submit to this project - http://tasks.pixelbazaar.net/task.aspx?id=493261)
- Envelope (please submit to this project - http://tasks.pixelbazaar.net/task.aspx?id=493261)

My practice name (within my logo) is:
Marcus T. Benning, D.D.S., P.A.
Family and Cosmetic Dentistry

***Obviously you will notice that the lower leg of the "B" in my logo is a smile.

My new address and contact information is:
340 Larchmont Medical Lane, Suite 112
Cary, NC 27604

919-472-3815 (ph)
919-472-3827 (fax)
www.benningdds.net

If you would like to use a tagline, I would suggest "Precision Dentistry with a Personal Touch".

I have attached my logo in numerous formats - please download attached logos here - http://tasks.pixelbazaar.net/task.aspx?id=493261

I have also attached 2 QR codes, one of which links to my website and the other one which links to a "Like" page for my business Chatterly page. These QR codes could be improved by putting a graphic in the middle, but I created these myself and did not know how to do this.

Thank you for your time. I look forward to seeing all of your creative ideas!

Depending on the designs, I may award 2 different winners for the Business Card project and the Stationery Project. Or if a design is really good, I will award both projects to the same designer.

Reason: Initially I had bundled my entire project (stationary, envelope, business card, etc.) into one contest but PixelBazaar has recommended that I split it into two distinct projects (business card AND stationary, envelope, etc.). Therefore I'm extending the deadline so that I receive enough designs. Thank you.

Target Market(s)

Current and prospective dental patients.

Industry/Entity Type

Dental

Requirements
Must have
• Please ensure business card has a 2-sided design.
Please ensure that your design is "practical" for printing purposes.
Nice to have
• Improvement of QR codes by addition of graphics in the middle to differentiate them. Incorporation of QR codes into business card design, maybe on the back side?

```html
<!DOCTYPE html>
<html lang="en">
<head>
<meta charset="utf-8">
<title>Business Card – Marcus T. Benning, D.D.S., P.A.</title>
<link href="https://fonts.googleapis.com/css2?family=Aldrich&display=swap" rel="stylesheet">
<style>
  :root {
    --page-bg: #e9ebec;
    --card-white: #ffffff;
    --teal-light: #22a39c;
    --teal-dark: #0d7472;
    --navy: #2a2f72;
    --ink-white: #ffffff;
    --tag-teal: #17857f;
    --card-shadow: rgba(20, 40, 50, 0.18);
  }
  * { box-sizing: border-box; margin: 0; padding: 0; }
  html, body {
    width: 1200px; height: 900px; overflow: hidden;
    background: var(--page-bg);
    font-family: "Aldrich", "Trebuchet MS", sans-serif;
  }
  .sheet {
    width: 1200px; height: 900px;
    display: flex; flex-direction: column; align-items: center; justify-content: center;
    gap: 48px;
  }
  .card {
    position: relative;
    width: 640px; height: 366px;
    border-radius: 30px;
    background: var(--card-white);
    overflow: hidden;
    box-shadow: 0 10px 28px var(--card-shadow);
  }
  .card__wave { position: absolute; inset: 0; width: 100%; height: 100%; }

  .practice-mark {
    position: absolute;
    display: flex; align-items: center; gap: 10px;
  }
  .practice-mark__square {
    width: 30px; height: 30px; background: var(--navy); flex: none;
  }
  .practice-mark__name {
    color: var(--navy); font-size: 17px; letter-spacing: 0.5px; white-space: nowrap;
  }
  .practice-mark__tagline {
    display: block; margin-top: 3px;
    color: var(--tag-teal); font-size: 9px; letter-spacing: 1.2px; text-transform: uppercase;
    border-top: 1px solid var(--navy); padding-top: 3px;
  }
  .card--front .practice-mark { top: 36px; left: 170px; }

  .holder {
    position: absolute; left: 40px; top: 178px; color: var(--ink-white);
  }
  .holder__name { font-size: 16px; letter-spacing: 1px; text-transform: uppercase; }
  .holder__role { font-size: 10.5px; letter-spacing: 1px; margin-top: 4px; text-transform: uppercase; }
  .holder__address { margin-top: 18px; font-size: 11px; line-height: 1.6; letter-spacing: 0.5px; }

  .contact-list {
    position: absolute; right: 34px; top: 276px;
    list-style: none; color: var(--ink-white); font-size: 11.5px; letter-spacing: 0.4px;
  }
  .contact-list__item {
    display: flex; align-items: center; justify-content: flex-end; gap: 8px; height: 20px;
  }
  .contact-list__icon { width: 12px; height: 12px; flex: none; }

  .card--back .practice-mark {
    top: 50%; left: 50%; transform: translate(-50%, -50%);
  }
  .card--back .practice-mark__square { width: 40px; height: 40px; }
  .card--back .practice-mark__name { font-size: 22px; }
  .card--back .practice-mark__tagline { font-size: 11px; }
</style>
</head>
<body>
<main class="sheet">

  <section class="card card--front" aria-label="Business card front">
    <svg class="card__wave" viewBox="0 0 640 366" preserveAspectRatio="none" aria-hidden="true">
      <defs>
        <linearGradient id="tealFill" x1="0" y1="0" x2="1" y2="1">
          <stop offset="0" stop-color="#22a39c"/>
          <stop offset="1" stop-color="#0d7472"/>
        </linearGradient>
      </defs>
      <path d="M0,142 C180,160 420,214 640,222 L640,366 L0,366 Z" fill="url(#tealFill)"/>
      <path d="M0,138 C180,156 420,210 640,218" fill="none" stroke="#2a2f72" stroke-width="6"/>
    </svg>

    <div class="practice-mark">
      <span class="practice-mark__square"></span>
      <span class="practice-mark__name">MARCUS T. BENNING, D.D.S., P.A.
        <span class="practice-mark__tagline">Family and Cosmetic Dentistry</span>
      </span>
    </div>

    <div class="holder">
      <p class="holder__name">Marcus T. Benning</p>
      <p class="holder__role">Family Dentist</p>
      <p class="holder__address">340 Larchmont Medical Lane, Suite 112<br>Cary, NC 27604</p>
    </div>

    <ul class="contact-list">
      <li class="contact-list__item">919-472-3815
        <svg class="contact-list__icon" viewBox="0 0 12 12"><path d="M2.5 1 L4.5 1 L5.3 3.6 L4 4.6 C4.7 6 6 7.3 7.4 8 L8.4 6.7 L11 7.5 L11 9.5 C11 10.3 10.3 11 9.5 11 C5 11 1 7 1 2.5 C1 1.7 1.7 1 2.5 1 Z" fill="#ffffff"/></svg>
      </li>
      <li class="contact-list__item">919-472-3827
        <svg class="contact-list__icon" viewBox="0 0 12 12"><rect x="1" y="4" width="10" height="6" rx="1" fill="#ffffff"/><rect x="3" y="1" width="6" height="3" fill="none" stroke="#ffffff" stroke-width="1"/></svg>
      </li>
      <li class="contact-list__item">www.benningdds.net
        <svg class="contact-list__icon" viewBox="0 0 12 12"><circle cx="6" cy="6" r="5" fill="none" stroke="#ffffff" stroke-width="1.1"/><ellipse cx="6" cy="6" rx="2.2" ry="5" fill="none" stroke="#ffffff" stroke-width="1"/><path d="M1 6 H11" stroke="#ffffff" stroke-width="1"/></svg>
      </li>
    </ul>
  </section>

  <section class="card card--back" aria-label="Business card back">
    <div class="practice-mark">
      <span class="practice-mark__square"></span>
      <span class="practice-mark__name">MARCUS T. BENNING, D.D.S., P.A.
        <span class="practice-mark__tagline">Family and Cosmetic Dentistry</span>
      </span>
    </div>
  </section>

</main>
</body>
</html>
```